Sprinkles & Tails 2nd Annual Fundraiser

I am a Realtor sponsoring the 2nd annual fundraiser on behalf of Allies of Harlow Vale Animal Haven. Like the flyer to be professional yet fun and inviting. Please see the attached file below. The 1st annual flyer was fun but not as professional, modern or inviting as I would have liked it to be.
Target Market(s)
Dog lovers in Ponte Vedra, Ponte Vedra Beach and Nocatee Florida
Logo Text
Needed
Font styles to use
Other font styles liked:
- Font that fits the style of the fundraiser
Colors
886aae
abd036
Requirements
Must have
- Please see the attached flyer and photos.
- This will be the 2nd Annual on Saturday, April 27, 2019 from 10AM - 1PM. Same location: Kendrick Realty, 418 Tillbrook Ave. Ponte Vedra FL 32075

```html
<!DOCTYPE html>
<html lang="en">
<head>
<meta charset="utf-8">
<title>Sprinkles &amp; Tails Doggie Wash Extravaganza</title>
<link href="https://fonts.googleapis.com/css2?family=Lobster&family=Courgette&family=Open+Sans:wght@400;600;700&display=swap" rel="stylesheet">
<style>
  :root{
    --purple:#6a2c91;
    --purple-soft:#886aae;
    --green:#abd036;
    --green-light:#cfe27e;
    --sky-top:#bfe3f5;
    --sky-bottom:#eef8fc;
    --ink:#2d2d2d;
    --icon:#efe0a6;
    --white:#ffffff;
    --page:#d6d6d6;
  }
  *{margin:0;padding:0;box-sizing:border-box}
  html,body{width:1200px;height:2250px;overflow:hidden;background:var(--page)}
  .flyer{
    position:absolute;left:50px;top:348px;width:466px;height:658px;
    transform:scale(2.3605);transform-origin:0 0;overflow:hidden;
    font-family:"Open Sans",sans-serif;color:var(--ink);
    box-shadow:0 1px 4px rgba(0,0,0,.25);
  }
  .flyer-backdrop{position:absolute;inset:0}
  .event-title{
    position:absolute;top:14px;left:0;width:100%;text-align:center;
    font-family:"Lobster",cursive;color:var(--purple);
    font-size:23px;line-height:29px;font-weight:400;
  }
  .photo{
    position:absolute;border-radius:50%;border:3px solid var(--white);
    box-shadow:0 1px 3px rgba(0,0,0,.2);
  }
  .photo--volunteer{left:133px;top:118px;width:110px;height:110px;background:radial-gradient(circle at 40% 60%,#a8713f,#6b6f74 55%,#d7d9dc)}
  .photo--dog{left:292px;top:118px;width:92px;height:92px;background:radial-gradient(circle at 50% 55%,#8c8378,#c9c3b6 50%,#e6e2dc)}
  .photo--wash-a{left:162px;top:367px;width:76px;height:76px;background:radial-gradient(circle,#7d8a76,#c8c7bf)}
  .photo--wash-b{left:260px;top:367px;width:76px;height:76px;background:radial-gradient(circle,#9a6a3d,#b9c8b0)}
  .photo--wash-c{left:358px;top:367px;width:76px;height:76px;background:radial-gradient(circle,#7a5a67,#b7a7a6)}
  .details-pill{
    position:absolute;left:22px;top:258px;width:115px;height:233px;
    background:var(--purple);border-radius:56px;color:var(--white);
    text-align:center;font-size:8.3px;line-height:11px;font-weight:600;
  }
  .details-pill svg{display:block;margin:0 auto}
  .detail{position:absolute;left:0;width:100%}
  .detail--date{top:16px}
  .detail--time{top:92px}
  .detail--place{top:152px}
  .detail p{margin-top:5px}
  .tagline{
    position:absolute;left:312px;top:226px;font-family:"Courgette",cursive;
    color:var(--purple);font-size:9.5px;
  }
  .support-label{position:absolute;left:328px;top:244px;font-size:10.5px;font-weight:600;color:var(--ink)}
  .charity-mark{
    position:absolute;left:318px;top:264px;width:82px;height:58px;border-radius:50%;
    background:var(--white);border:2px solid var(--purple);
    display:flex;align-items:center;justify-content:center;text-align:center;
    font-size:7px;line-height:9px;font-weight:700;color:var(--purple);padding:0 8px;
  }
  .perks{
    position:absolute;left:150px;top:272px;width:180px;list-style:none;
    font-size:9.3px;line-height:13.5px;font-weight:600;text-align:center;color:var(--ink);
  }
  .perks li::before{
    content:"";display:inline-block;width:7px;height:4px;margin-right:5px;
    border-left:1.8px solid var(--purple);border-bottom:1.8px solid var(--purple);
    transform:rotate(-45deg) translateY(-2px);
  }
  .donate-bar{
    position:absolute;left:150px;top:455px;width:296px;height:31px;border-radius:15px;
    background:var(--purple);color:var(--white);text-align:center;
    font-size:8.3px;line-height:10.5px;font-weight:600;padding-top:5px;
  }
  .guest-note{
    position:absolute;left:140px;top:491px;width:316px;text-align:center;
    font-size:8.3px;line-height:11px;font-weight:600;color:var(--ink);
  }
  .guest-note em{font-family:"Courgette",cursive;font-style:normal;color:var(--purple)}
  .mascot{
    position:absolute;left:348px;top:516px;width:118px;height:142px;
    border-radius:60px 0 0 0;background:linear-gradient(160deg,#9b5a2d,#6e3d1c 60%,#c9c4bd);
  }
  .contact{position:absolute;top:552px;text-align:center;font-size:7px;line-height:9.5px;color:var(--ink)}
  .contact--realtor{left:50px;width:140px}
  .contact--charity{left:200px;width:130px}
  .contact-mark{font-weight:600;color:var(--purple);font-size:10px;line-height:12px;margin-bottom:6px}
  .contact--charity .contact-mark{font-size:7.5px;line-height:9px}
</style>
</head>
<body>
<main class="flyer">
  <svg class="flyer-backdrop" viewBox="0 0 466 658" width="466" height="658" aria-hidden="true">
    <defs>
      <linearGradient id="sky" x1="0" y1="0" x2="0" y2="1">
        <stop offset="0" stop-color="var(--sky-top)"/>
        <stop offset="1" stop-color="var(--sky-bottom)"/>
      </linearGradient>
      <linearGradient id="meadow" x1="0" y1="0" x2="1" y2="0.4">
        <stop offset="0" stop-color="#a3c930"/>
        <stop offset="0.6" stop-color="var(--green)"/>
        <stop offset="1" stop-color="var(--green-light)"/>
      </linearGradient>
      <linearGradient id="footer" x1="0" y1="0" x2="0" y2="1">
        <stop offset="0" stop-color="#ffffff"/>
        <stop offset="1" stop-color="#e9e9ec"/>
      </linearGradient>
    </defs>
    <rect width="466" height="658" fill="url(#sky)"/>
    <path d="M0 232 C120 200 250 190 466 92 V560 H0 Z" fill="var(--purple)"/>
    <path d="M0 250 C120 216 260 206 466 108 V560 H0 Z" fill="#1e1a22"/>
    <path d="M0 256 C120 222 262 212 466 116 V560 H0 Z" fill="var(--white)"/>
    <path d="M0 262 C120 230 262 220 466 124 V560 H0 Z" fill="url(#meadow)"/>
    <path d="M150 262 C230 200 330 215 466 160 V300 C380 300 260 320 150 262 Z" fill="#b9d84f" opacity=".5"/>
    <path d="M0 538 C150 516 320 516 466 530 V658 H0 Z" fill="url(#footer)"/>
    <path d="M0 538 C150 516 320 516 466 530" fill="none" stroke="var(--purple)" stroke-width="2.5"/>
    <path d="M0 545 C150 525 320 524 466 536" fill="none" stroke="var(--purple-soft)" stroke-width="1"/>
  </svg>

  <h1 class="event-title">Second Annual<br>Sprinkles &amp; Tails<br>Doggie Wash Extravaganza</h1>

  <div class="photo photo--volunteer" role="img" aria-label="Photo of a volunteer with a brown dog beside the event sign"></div>
  <div class="photo photo--dog" role="img" aria-label="Photo of a shaggy grey dog wearing a pink bandana"></div>

  <aside class="details-pill">
    <div class="detail detail--date">
      <svg width="26" height="26" viewBox="0 0 26 26" fill="none" stroke="var(--icon)" stroke-width="1.4">
        <rect x="3" y="5" width="20" height="18" rx="2"/><path d="M3 10H23M8 3V7M18 3V7M7 14H10M12 14H15M17 14H20M7 18H10M12 18H15"/>
      </svg>
      <p>Saturday,<br>27th April, 2019</p>
    </div>
    <div class="detail detail--time">
      <svg width="26" height="26" viewBox="0 0 26 26" fill="none" stroke="var(--icon)" stroke-width="1.4">
        <circle cx="13" cy="13" r="10"/><path d="M13 7V13L17 16"/>
      </svg>
      <p>10AM to 1PM</p>
    </div>
    <div class="detail detail--place">
      <svg width="26" height="26" viewBox="0 0 26 26" fill="none" stroke="var(--icon)" stroke-width="1.4">
        <path d="M13 24C13 24 5 15 5 10A8 8 0 0 1 21 10C21 15 13 24 13 24Z"/><circle cx="13" cy="10" r="3"/>
      </svg>
      <p>Kendrick Realty,<br>418 Tillbrook Ave.<br>Ponte Vedra FL 32075</p>
    </div>
  </aside>

  <p class="tagline">A Family Fun Event for All Ages</p>
  <p class="support-label">In Support of</p>
  <div class="charity-mark">Allies of Harlow Vale Animal Haven</div>

  <ul class="perks">
    <li>FREE Doggie Wash</li>
    <li>Raffle Drawings</li>
    <li>Food &amp; Beverages</li>
    <li>Grand Prize</li>
    <li>Vendors (FREE give-a-ways)</li>
    <li>Donations Welcome</li>
  </ul>

  <div class="photo photo--wash-a" role="img" aria-label="Photo of guests washing dogs outdoors"></div>
  <div class="photo photo--wash-b" role="img" aria-label="Photo of the costumed mascot greeting a visitor"></div>
  <div class="photo photo--wash-c" role="img" aria-label="Photo of volunteers bathing a dog"></div>

  <p class="donate-bar">To make a donation: https://www.harlowvalehaven.org/give/<br>click: Donate</p>
  <p class="guest-note">All domestic breeds from puppies to seniors invited. Please be sure <em>Furry Fido</em> is tolerant of other dogs, crowds and bathing.</p>

  <div class="mascot" role="img" aria-label="Photo of the event's costumed dog mascot"></div>

  <address class="contact contact--realtor" style="font-style:normal">
    <p class="contact-mark">Kendrick Realty</p>
    <p>Marlene Pryce</p>
    <p>Kendrick Realty Corp.</p>
    <p>770.555.0147</p>
    <p>marlenepryce@kendrickrealtycorp.com</p>
  </address>
  <address class="contact contact--charity" style="font-style:normal">
    <p class="contact-mark">Allies of Harlow Vale<br>Animal Haven</p>
    <p>Denise Calloway</p>
    <p>AHVAH</p>
    <p>904.555.0183</p>
    <p>denise-calloway@mailhaven.net</p>
  </address>
</main>
</body>
</html>
```